RM Tomás Rivera (Business Card)

Hi designers, in this work, I'm looking for an sophisticated stylish, elegant and proffesional personal card. We have a laboratory of pathology automated, with equipments high quality.
In this web the designers, have created my business logo, the name is "RM Tomás Rivera"
In our lab, we principal work is to prepare the biopsies for further diagnostic of diseases like cancer, tumors, etc.
I need that the first face, only having my complete logo (Rm Tomás Rivera, Laboratorio de procesamiento Histologico)
The overleaf, could repeat the same logo, like water logo.
In this face, I need to say: My full data:

Técnico en Anatomía Patológica
Tomás Rivera Ibarra M.P 47203
Av. Paredes Luján 418 - 2do piso - Instituto Marbel.
Córdoba, Argentina
(0351) 154820937
rivera.tomas@correolab.example

with respect the colors of card, use your imagination, the original logo color is violet, I haven't chosen a color base for the card.

attached pictures are examples of cards I like your DESIGN.
Attached too, the original logo to my company.

the size of card are:
horizontal: 9cm
vertical: 5,5cm

any question that you have, not doubt to question me,
Hand to work!

Industry/Entity Type

Laboratory

Requirements
Must have
• designers sophisticated, not simples, like show the images attached

```html
<!DOCTYPE html>
<html lang="es">
<head>
<meta charset="utf-8">
<title>Tomás Rivera — Tarjeta personal</title>
<link rel="stylesheet" href="https://fonts.googleapis.com/css2?family=Open+Sans:wght@400;600;700&family=Pathway+Gothic+One&family=Montserrat:wght@300;400&display=swap">
<style>
  :root {
    --violet: #6a2f96;
    --violet-soft: #8a5cb8;
    --paper: #ffffff;
    --steel: #7d8185;
    --steel-light: #9a9ea2;
    --steel-dark: #5f6367;
    --rule: #4a4d50;
    --ink-grey: #6f7276;
    --stage: #e9e8ea;
  }
  * { box-sizing: border-box; margin: 0; padding: 0; }
  html, body { width: 1200px; height: 960px; overflow: hidden; }
  body {
    background: var(--stage);
    display: flex;
    flex-direction: column;
    align-items: center;
    justify-content: center;
    gap: 56px;
    font-family: "Open Sans", sans-serif;
  }
  .card {
    width: 640px;
    height: 391px;
    border-radius: 26px;
    overflow: hidden;
    position: relative;
    box-shadow: 0 6px 18px rgba(0,0,0,0.18);
  }

  /* Front: identity + details */
  .card-front { background: var(--paper); }
  .front-brand {
    height: 218px;
    display: flex;
    flex-direction: column;
    align-items: center;
    justify-content: flex-end;
    padding-bottom: 22px;
    gap: 16px;
  }
  .brand-name {
    display: flex;
    align-items: center;
    gap: 14px;
    font-family: "Montserrat", sans-serif;
    font-weight: 400;
    font-size: 24px;
    letter-spacing: 0.32em;
    color: var(--violet);
  }
  .brand-square {
    width: 34px;
    height: 34px;
    background: var(--violet);
  }
  .brand-tagline {
    font-family: "Pathway Gothic One", sans-serif;
    font-size: 30px;
    color: var(--ink-grey);
    letter-spacing: 0.01em;
  }
  .front-details {
    position: absolute;
    left: 0; right: 0; bottom: 0;
    top: 218px;
    background: linear-gradient(180deg, var(--steel-light) 0%, var(--steel) 100%);
    border-top: 5px solid var(--rule);
    padding: 18px 40px 0;
    color: #fff;
  }
  .holder-name {
    font-weight: 700;
    font-size: 21px;
    letter-spacing: 0.01em;
  }
  .holder-reg {
    font-weight: 400;
    font-size: 18px;
    color: var(--violet);
  }
  .holder-role {
    font-size: 15px;
    color: var(--violet);
    margin-top: 1px;
  }
  .contact-list {
    list-style: none;
    margin-top: 16px;
    font-size: 15px;
    line-height: 1.45;
  }
  .contact-label {
    display: inline-block;
    width: 26px;
    color: var(--violet);
    font-weight: 600;
  }
  .contact-address {
    margin-top: 12px;
    font-size: 14px;
  }

  /* Back: large name mark */
  .card-back {
    background: radial-gradient(ellipse at 62% 55%, #a9acaf 0%, var(--steel) 55%, var(--steel-dark) 100%);
    display: flex;
    align-items: center;
    justify-content: center;
  }
  .back-name {
    display: flex;
    align-items: center;
    gap: 18px;
    font-family: "Montserrat", sans-serif;
    font-weight: 300;
    font-size: 28px;
    letter-spacing: 0.4em;
    color: #fff;
  }
  .back-square {
    width: 40px;
    height: 40px;
    border: none;
    background: #fff;
  }
</style>
</head>
<body>
  <section class="card card-front" aria-label="Frente de la tarjeta">
    <div class="front-brand">
      <div class="brand-name"><span class="brand-square"></span>RM TOMÁS RIVERA</div>
      <div class="brand-tagline">LABORATORIO DE PROCESAMIENTO HISTOLOGICO</div>
    </div>
    <div class="front-details">
      <p><span class="holder-name">TOMÁS RIVERA IBARRA,</span> <span class="holder-reg">M.P 47203</span></p>
      <p class="holder-role">Técnico en Anatomía Patológica</p>
      <ul class="contact-list">
        <li><span class="contact-label">M:</span>(0351) 154820937</li>
        <li><span class="contact-label">E:</span>rivera.tomas@correolab.example</li>
      </ul>
      <p class="contact-address">Av. Paredes Luján 418 - 2do piso - Instituto Marbel. Córdoba, Argentina</p>
    </div>
  </section>

  <section class="card card-back" aria-label="Dorso de la tarjeta">
    <div class="back-name"><span class="back-square"></span>TOMÁS RIVERA</div>
  </section>
</body>
</html>
```